Visitenkarten-Design für moderne Steuerberatung
Zielgruppe
Treuhandgesellschaft, Steuerberatung, Unternehmensberatung, Buchhaltung
Zielgruppe sind KMU und Privatpersonen
Aufgabenstellung
modern, schlicht, übersichtlich

```html
<!DOCTYPE html>
<html lang="de">
<head>
<meta charset="utf-8">
<title>Valdrec Consulting – Visitenkarte</title>
<link rel="stylesheet" href="https://fonts.googleapis.com/css2?family=Open+Sans:wght@700&family=Saira:wght@400;600&display=swap">
<style>
  :root {
    --stage: #1b1b1b;
    --card: #ffffff;
    --brand-blue: #1f3a93;
    --mark-grey: #b3b3b3;
    --text-grey: #aaa69d;
    --tagline-grey: #555555;
    --rule-blue: #a4b9e8;
    --watermark: #eef1f8;
  }
  * { margin: 0; padding: 0; box-sizing: border-box; }
  html, body {
    width: 1200px;
    height: 947px;
    overflow: hidden;
    background: var(--stage);
  }
  .business-card {
    position: absolute;
    left: 130px;
    top: 170px;
    width: 940px;
    height: 608px;
    background: var(--card);
    overflow: hidden;
    font-family: "Saira", sans-serif;
  }
  .brand-dot {
    position: absolute;
    left: 58px;
    top: 68px;
    width: 168px;
    height: 168px;
    border-radius: 50%;
    background: var(--brand-blue);
  }
  .watermark-circle {
    position: absolute;
    left: 760px;
    top: 300px;
    width: 300px;
    height: 300px;
    border-radius: 50%;
    background: var(--watermark);
  }
  .brand-name {
    position: absolute;
    left: 266px;
    top: 70px;
    font-family: "Open Sans", sans-serif;
    font-weight: 700;
    font-size: 78px;
    line-height: 1;
    letter-spacing: -1px;
    color: var(--brand-blue);
  }
  .brand-tagline {
    position: absolute;
    left: 270px;
    top: 158px;
    font-size: 33px;
    line-height: 1;
    color: var(--tagline-grey);
  }
  .divider {
    position: absolute;
    left: 272px;
    top: 232px;
    right: 0;
    height: 2px;
    background: var(--rule-blue);
  }
  .contact {
    position: absolute;
    left: 276px;
    top: 272px;
    color: var(--text-grey);
    font-size: 30px;
    line-height: 38px;
  }
  .company-name {
    font-weight: 600;
    font-size: 33px;
    color: var(--brand-blue);
    margin-bottom: 22px;
  }
  .contact-group { margin-bottom: 8px; }
  .contact-group.web { font-size: 27px; line-height: 38px; }
</style>
</head>
<body>
  <div class="business-card">
    <div class="watermark-circle" aria-hidden="true"></div>
    <div class="brand-dot" aria-hidden="true"></div>
    <div class="brand-name">VALDREC</div>
    <div class="brand-tagline">Treuhand &amp; Consulting</div>
    <div class="divider"></div>
    <div class="contact">
      <div class="company-name">Valdrec Consulting GmbH</div>
      <div class="contact-group">
        <div>Lindenweg 7</div>
        <div>8412 Hornach</div>
      </div>
      <div class="contact-group">
        <div>Tel. 071 480 23 60</div>
        <div>Fax 071 480 23 61</div>
      </div>
      <div class="contact-group web">
        <div>info@valdrecconsulting.ch</div>
        <div>www.valdrecconsulting.ch</div>
      </div>
    </div>
  </div>
</body>
</html>
```